vQ CARELINE (Brochure Design)

i need a proffesional brochure made. we are a mobile medical service company providing mobile Arterial Blood Gases(ABG's). Respiratory & Ventilator Consultation services. Ventilator and Tracheostomy training courses. and mobile vaccine administration.

this is my first time making a brochure so any and all advice/guidance will be appreciated.

i am thinking prints will be 8.5 inches x 11 inches (TRI-FOLD and BI-FOLD)

i have uploaded my business card design and logo design for reference.
as this brochure project continues ill update needs of the project descriptions.

Introduction: At vq CARELINE, we're dedicated to enhancing healthcare services by providing exceptional mobile arterial blood gases, respiratory and ventilator consultation services. Our core values revolve around excellence, compassion and accessibility. We believe that every individual deserves the highest standard of care, and we're committed to delivering that through expert guidance and top-notch training courses. Your health is at the heart of what we do, and we're here to support you on your journey to better respiratory health.

Mobile Arterial Blood Gases : Our mobile Arterial Blood Gas service offers quick, on-the-spot analysis of pH, oxygen, and carbon dioxide levels in your the blood. This service enables rapid adjustments to treatment plans for more effective respiratory care.

Ventilator and Tracheostomy Training: Our ventilator and tracheostomy course empowers caregivers and healthcare professionals to manage ventilators and care for tracheostomy patients with expertise. This training enhances patient safety, treatment outcomes, and healthcare provider confidence. vQ Careline your choice for top-notch care, convenience, and peace of mind.

Respiratory Consulting: Our respiratory consulting services provide expert guidance and support for individuals with respiratory / ventilator concerns. Benefits include personalized treatment plans, better management of respiratory conditions, and improved overall lung health. vQ Careline is your trusted partner for a breath of fresh air.

Target Market(s)

Sub-Acute facilities, Pulmonary Clinics, Pulmonologists, Nurses, Caregivers, Hospice and homehealth companies.

Industry/Entity Type

Medical; Respiratory; Nursing

Requirements
Must have
• proffesional simple design.

```html
<!DOCTYPE html>
<html lang="en">
<head>
<meta charset="utf-8">
<title>vQ CARELINE – Tri-fold Brochure</title>
<link href="https://fonts.googleapis.com/css2?family=Montserrat:wght@400;500;600&display=swap" rel="stylesheet">
<style>
  :root{
    --blue:#0a63b5;
    --green:#22a244;
    --white:#ffffff;
    --stage:#e3e3e7;
  }
  *{margin:0;padding:0;box-sizing:border-box}
  html,body{width:1200px;height:1200px;overflow:hidden;background:var(--stage);font-family:"Montserrat",sans-serif}
  .sheet{position:absolute;left:240px;width:719px;height:508px;overflow:hidden;background:var(--white)}
  .sheet--outside{top:54px}
  .sheet--inside{top:604px}
  .panel{position:absolute;top:0;width:240px;height:508px;overflow:hidden}
  .panel--1{left:0}.panel--2{left:240px}.panel--3{left:479px}
  .bg-blue{background:var(--blue)}.bg-green{background:var(--green)}.bg-white{background:var(--white)}
  .panel svg.art{position:absolute;left:0;top:0;width:240px;height:508px}
  .heading{position:absolute;left:23px;font-weight:600;font-size:28px;line-height:32.5px;color:var(--white);letter-spacing:.2px}
  .heading--green{color:var(--green)}
  .rule{position:absolute;left:0;height:11px;background:var(--white)}
  .rule--green{background:var(--green)}
  .body-copy{position:absolute;left:22px;font-size:9.2px;line-height:14.5px;color:var(--white);white-space:nowrap}
  .body-copy--green{color:var(--green)}
  .contact-title{position:absolute;left:0;width:240px;top:30px;text-align:center;color:var(--white);font-size:28px;font-weight:500}
  .contact-line{position:absolute;left:0;width:240px;text-align:center;color:var(--white);font-size:9.8px;line-height:16.5px}
  .brand{position:absolute;left:0;width:240px;top:36px;text-align:center}
  .brand__name{font-size:20px;font-weight:600;color:var(--blue);letter-spacing:1.5px}
  .cover-title{position:absolute;left:0;width:240px;text-align:center;color:var(--white);font-weight:600;font-size:27px;line-height:33px}
  .cover-title .hl{display:inline-block;background:var(--green);padding:0 7px;line-height:33px}
  .web-strip{position:absolute;left:0;top:483px;width:240px;height:15px;background:var(--white);text-align:center;font-size:8.6px;line-height:15px;color:var(--blue)}
  .services{position:absolute;left:15px;top:410px;color:var(--blue)}
  .services h3{font-size:12px;font-weight:600;margin-bottom:3px}
  .services ul{list-style:none}
  .services li{font-size:9.1px;line-height:14.6px;padding-left:9px;position:relative;white-space:nowrap}
  .services li::before{content:"";position:absolute;left:0;top:6px;width:3px;height:3px;border-radius:50%;background:var(--blue)}
</style>
</head>
<body>

<section class="sheet sheet--outside">
  <div class="panel panel--1 bg-blue">
    <h2 class="heading" style="top:22px">Respiratory<br>Consulting:</h2>
    <div class="rule" style="top:92px;width:199px"></div>
    <p class="body-copy" style="top:123px">Our respiratory consulting services provide<br>expert guidance and support for individuals<br>with respiratory / ventilator concerns. Bene-<br>fits include personalized treatment plans,<br>better management of respiratory condi-<br>tions, and improved overall lung health. vQ<br>Careline is your trusted partner for a breath of<br>fresh air.</p>
    <svg class="art" viewBox="0 0 240 508">
      <defs><linearGradient id="g-vent" x1="0" y1="0" x2="1" y2="1"><stop offset="0" stop-color="#e8eaf0"/><stop offset="1" stop-color="#b9bfd6"/></linearGradient></defs>
      <path d="M0 284 H165 A40 40 0 0 1 205 324 V412 A40 40 0 0 1 165 452 H0" fill="none" stroke="var(--white)" stroke-width="1.3"/>
      <path d="M0 291 H160 A40 40 0 0 1 200 331 V405 A40 40 0 0 1 160 445 H0 Z" fill="url(#g-vent)" role="img" aria-label="Photo of two portable ventilator units"/>
    </svg>
  </div>

  <div class="panel panel--2 bg-green">
    <h2 class="contact-title">Contact us</h2>
    <svg class="art" viewBox="0 0 240 508">
      <defs><linearGradient id="g-cpap" x1="0" y1="0" x2="1" y2="1"><stop offset="0" stop-color="#f4f6fa"/><stop offset="1" stop-color="#9fb5d6"/></linearGradient></defs>
      <circle cx="119" cy="102" r="20" fill="var(--white)"/>
      <rect x="113" y="91" width="12" height="21" rx="2.5" fill="none" stroke="var(--blue)" stroke-width="2"/>
      <line x1="117" y1="108.5" x2="121" y2="108.5" stroke="var(--blue)" stroke-width="1.5"/>
      <circle cx="119" cy="187" r="20" fill="var(--white)"/>
      <rect x="109" y="180" width="20" height="14" fill="var(--blue)"/>
      <path d="M109 180 L119 188 L129 180 M109 194 L116 187 M129 194 L122 187" fill="none" stroke="var(--white)" stroke-width="1.3"/>
      <circle cx="119" cy="270" r="20" fill="var(--white)"/>
      <path d="M111 270 L119 262 L127 270 V278 H122 V273 H116 V278 H111 Z" fill="var(--blue)"/>
      <circle cx="119" cy="449" r="97" fill="none" stroke="var(--white)" stroke-width="1.3"/>
      <circle cx="119" cy="449" r="89" fill="url(#g-cpap)" role="img" aria-label="Photo of two portable respiratory therapy devices"/>
    </svg>
    <p class="contact-line" style="top:127px">(000) 123 456 789</p>
    <p class="contact-line" style="top:216px">info@yourcompany.com</p>
    <p class="contact-line" style="top:299px">Address Line Here, 15<br>City (Country)</p>
  </div>

  <div class="panel panel--3 bg-white">
    <svg class="art" viewBox="0 0 240 508">
      <defs><linearGradient id="g-patient" x1="0" y1="0" x2="0" y2="1"><stop offset="0" stop-color="#eef2f7"/><stop offset="1" stop-color="#8eaad2"/></linearGradient></defs>
      <rect x="0" y="232" width="240" height="276" fill="var(--blue)"/>
      <path d="M19 232 V263 A98.5 98.5 0 0 0 216 263 V232" fill="none" stroke="var(--white)" stroke-width="1.5"/>
      <path d="M27 187 A91 91 0 0 1 209 187 V264 A91 91 0 0 1 27 264 Z" fill="url(#g-patient)" role="img" aria-label="Photo of a patient resting in a hospital bed beside a ventilator"/>
    </svg>
    <div class="brand"><span class="brand__name">vQ CARELINE</span></div>
    <h1 class="cover-title" style="top:378px">MOBILE<br><span class="hl">MEDICAL</span><br>SERVICES</h1>
    <div class="web-strip">www.vqcareline.com</div>
  </div>
</section>

<section class="sheet sheet--inside">
  <div class="panel panel--1 bg-white">
    <svg class="art" viewBox="0 0 240 508">
      <defs>
        <linearGradient id="g-abg" x1="0" y1="0" x2="1" y2="1"><stop offset="0" stop-color="#f0e4de"/><stop offset="1" stop-color="#4a78d0"/></linearGradient>
        <clipPath id="clip-top"><rect x="0" y="0" width="240" height="338"/></clipPath>
        <clipPath id="clip-bottom"><rect x="0" y="338" width="240" height="170"/></clipPath>
      </defs>
      <rect x="0" y="0" width="240" height="338" fill="var(--green)"/>
      <circle cx="109" cy="332" r="67" fill="none" stroke="var(--white)" stroke-width="1.3" clip-path="url(#clip-top)"/>
      <circle cx="109" cy="332" r="67" fill="none" stroke="var(--green)" stroke-width="1.3" clip-path="url(#clip-bottom)"/>
      <circle cx="109" cy="332" r="60" fill="url(#g-abg)" role="img" aria-label="Photo of a gloved clinician drawing an arterial blood sample from a wrist"/>
    </svg>
    <h2 class="heading" style="top:23px">Introduction</h2>
    <div class="rule" style="top:64px;width:199px"></div>
    <p class="body-copy" style="top:86px">At vq CARELINE, we're dedicated to enhanc-<br>ing healthcare services by providing excep-<br>tional mobile arterial blood gases, respiratory<br>and ventilator consultation services. Our core<br>values revolve around excellence, compas-<br>sion and accessibility. We believe that every<br>individual deserves the highest standard of<br>care, and we're committed to delivering that<br>through expert guidance and top-notch<br>training courses. Your health is at the heart of<br>what we do, and we're here to support you<br>on your journey to better respiratory health.</p>
    <div class="services">
      <h3>SERVICES</h3>
      <ul>
        <li>Mobile Arterial Blood Gases(ABG's).</li>
        <li>Respiratory &amp; Ventilator Consultation services.</li>
        <li>Ventilator and Tracheostomy training courses.</li>
        <li>Mobile vaccine administration.</li>
      </ul>
    </div>
  </div>

  <div class="panel panel--2 bg-blue">
    <svg class="art" viewBox="0 0 240 508">
      <defs><linearGradient id="g-syringe" x1="0" y1="0" x2="1" y2="1"><stop offset="0" stop-color="#4c5878"/><stop offset=".6" stop-color="#d9b4a2"/><stop offset="1" stop-color="#eef4f6"/></linearGradient></defs>
      <path d="M14 0 H240 V120 Q240 232 128 232 Q14 232 14 120 Z" fill="url(#g-syringe)" role="img" aria-label="Photo of a syringe drawing arterial blood from a patient's wrist"/>
    </svg>
    <h2 class="heading" style="top:257px">Mobile<br>Arterial<br>Blood Gases :</h2>
    <div class="rule" style="top:358px;width:207px"></div>
    <p class="body-copy" style="top:384px">Our mobile Arterial Blood Gas service offers<br>quick, on-the-spot analysis of pH, oxygen,<br>and carbon dioxide levels in your the blood.<br>This service enables rapid adjustments to<br>treatment plans for more effective respirato-<br>ry care.</p>
  </div>

  <div class="panel panel--3 bg-white">
    <svg class="art" viewBox="0 0 240 508">
      <defs><linearGradient id="g-nurse" x1="0" y1="0" x2="1" y2="0"><stop offset="0" stop-color="#7a5a8e"/><stop offset=".5" stop-color="#c8b8ad"/><stop offset="1" stop-color="#5d7bb4"/></linearGradient></defs>
      <rect x="0" y="340" width="240" height="168" fill="var(--green)"/>
      <path d="M240 350 H89 A38 38 0 0 0 51 388 V462 A38 38 0 0 0 89 500 H240" fill="none" stroke="var(--white)" stroke-width="1.3"/>
      <path d="M240 355 H92 A36 36 0 0 0 56 391 V459 A36 36 0 0 0 92 495 H240 Z" fill="url(#g-nurse)" role="img" aria-label="Photo of a nurse adjusting a ventilator beside a patient's bed"/>
    </svg>
    <h2 class="heading heading--green" style="top:23px">Ventilator and<br>Tracheostomy<br>Training:</h2>
    <div class="rule rule--green" style="top:127px;width:204px"></div>
    <p class="body-copy body-copy--green" style="top:169px">Our ventilator and tracheostomy course<br>empowers caregivers and healthcare profes-<br>sionals to manage ventilators and care for<br>tracheostomy patients with expertise. This<br>training enhances patient safety, treatment<br>outcomes, and healthcare provider confi-<br>dence. vQ Careline your choice for top-notch<br>care, convenience, and peace of mind.</p>
  </div>
</section>

</body>
</html>
```